A4 Simple eye catching special offers page with minimal text

I would like an A4 page to advertise my special offers on for sale sign boards. I want my logo on the design and maybe some pictures i have attached, or maybe a design without the pictures i might like the design with or without them. The following text should be used:
Free boards
Free rebrand
Read on to find out more

Target Market(s)

Businesses

Industry/Entity Type

Real Estate Agent

Requirements
Must have
• good design
Nice to have
• eye catching

```html
<!DOCTYPE html>
<html lang="en">
<head>
<meta charset="utf-8">
<title>Free Boards, Free Rebrand – Special Offer Flyer</title>
<link rel="stylesheet" href="https://fonts.googleapis.com/css2?family=Figtree:wght@500;600;700;800&display=swap">
<style>
  :root {
    --page-bg: #d7d7dc;
    --paper: #ffffff;
    --navy: #2b2a52;
    --red: #e3222e;
    --red-soft: #f2505a;
    --pink: #f5637a;
    --grey-text: #9a9a9a;
    --rule: #e6e8e8;
  }
  * { margin: 0; padding: 0; box-sizing: border-box; }
  html, body {
    width: 1200px;
    height: 1196px;
    overflow: hidden;
    background: var(--page-bg);
  }
  .flyer {
    position: absolute;
    left: 202px;
    top: 38px;
    width: 795px;
    height: 1120px;
    background: var(--paper);
    box-shadow: 0 2px 6px rgba(0,0,0,0.18);
  }
  .flyer svg { display: block; width: 100%; height: 100%; }
  .intro, .outro {
    font-family: "Figtree", sans-serif;
    font-weight: 600;
    font-size: 30px;
    fill: var(--grey-text);
  }
  .offer {
    font-family: "Figtree", sans-serif;
    font-weight: 800;
    font-size: 84px;
    fill: var(--navy);
    letter-spacing: -0.5px;
  }
  .web-link {
    font-family: "Figtree", sans-serif;
    font-weight: 700;
    font-size: 18px;
    fill: #ffffff;
  }
  .contact {
    font-family: "Figtree", sans-serif;
    font-weight: 500;
    font-size: 13px;
    fill: var(--navy);
  }
</style>
</head>
<body>
  <article class="flyer">
    <svg viewBox="0 0 903 1272" preserveAspectRatio="none" xmlns="http://www.w3.org/2000/svg">
      <defs>
        <linearGradient id="signs-tones" x1="0" y1="0" x2="1" y2="0.4">
          <stop offset="0" stop-color="#d9413a"/>
          <stop offset="0.2" stop-color="#1aa3b5"/>
          <stop offset="0.42" stop-color="#e8b84a"/>
          <stop offset="0.6" stop-color="#2f5fb0"/>
          <stop offset="0.8" stop-color="#d2e04a"/>
          <stop offset="1" stop-color="#5b2a7a"/>
        </linearGradient>
      </defs>

      <!-- header photo area -->
      <polygon class="header-photo" role="img"
        aria-label="Photo of a row of colourful estate agent for-sale signs"
        fill="url(#signs-tones)"
        points="0,0 903,0 903,330 623,377 0,492"/>

      <!-- red accent bands -->
      <polygon class="accent-red" fill="var(--red)" points="356,325 903,205 903,325 623,377 356,427"/>
      <polygon class="accent-soft" fill="var(--red-soft)" opacity="0.85" points="548,300 903,220 903,255 548,345"/>
      <polygon class="accent-pink" fill="var(--pink)" opacity="0.6" points="440,380 820,312 820,342 440,410"/>
      <polygon class="accent-pink" fill="var(--pink)" opacity="0.55" points="703,245 903,200 903,250 703,296"/>

      <!-- navy corner -->
      <polygon class="accent-navy" fill="var(--navy)" points="623,377 903,322 903,500"/>

      <!-- roof-line rule and white body -->
      <polygon class="roof-rule" fill="var(--rule)" points="0,492 623,377 903,500 903,518 623,393 0,510"/>
      <polygon class="body" fill="var(--paper)" points="0,510 623,393 903,518 903,1272 0,1272"/>

      <!-- offer copy -->
      <text class="intro" x="183" y="710">switch to us and get</text>

      <path class="tick" fill="var(--red)"
        d="M72,772 Q86,770 96,795 Q118,752 150,733 Q120,765 100,808 Q90,812 86,808 Q80,785 72,772 Z"/>
      <text class="offer" x="180" y="802">FREE BOARDS</text>

      <path class="tick" fill="var(--red)"
        d="M72,893 Q86,891 96,916 Q118,873 150,854 Q120,886 100,929 Q90,933 86,929 Q80,906 72,893 Z"/>
      <text class="offer" x="180" y="907">FREE REBRAND</text>

      <text class="outro" x="183" y="966">read on to find out more</text>

      <!-- footer corner -->
      <polygon class="footer-red" fill="var(--red)" points="0,1092 293,1272 0,1272"/>
      <polygon class="footer-navy" fill="var(--navy)" points="0,1122 208,1272 0,1272"/>

      <rect class="web-box" x="59.5" y="1183.5" width="250" height="50" fill="var(--navy)" stroke="var(--red)" stroke-width="3"/>
      <text class="web-link" x="184.5" y="1215" text-anchor="middle">www.NorthSign.co.uk</text>

      <text class="contact" x="355" y="1204">Unit 14, Mill Lane Business Park</text>
      <text class="contact" x="355" y="1220">Mill Lane, Oakford, Westshire, OF12 3AB</text>
      <rect class="contact-divider" x="654" y="1192" width="2" height="30" fill="var(--red)"/>
      <text class="contact" x="678" y="1204">0300 5550147</text>
      <text class="contact" x="678" y="1220">info@northsign.co.uk</text>
    </svg>
  </article>
</body>
</html>
```